Vallecrestia Car Wrap Design. Hospitality and fashion company on the Alps.

Vallecrestia is an important reality in hospitality and fashion industry with 3 hotels and 5 boutiques in Livigno. Over half a century of history and tradition is their distinctive feature, a guarantee of quality and attention to detail, able to satisfy the most demanding customers.

We have recently developed a new corporate image and now we are ready to enhance our brand visibility by updating and customizing our company VAN.

The Van we want to wrap is a BLACK Halvard Tessin, lange Version, 2 Schiebetueren (2010). I attached the correct file to work on.

I also attached the new corporate brand-book (logo - colors - font and more).

NB: it is not possible to apply films on the plastic parts. It would be better to avoid that letters and small details go on the areas that have protrusions / recesses.

I received just 10 designs.....

Industry/Entity Type

Hotel & Fashion

Font styles to use
Other font styles liked:
• BRANDON GROTESQUE

Requirements
Must have
• logo - rhombuses. The Van is BLACK.
Nice to have
• mountains (not mandatory). You can find an example in the uploaded documents.
Should not have
• It is not possible to apply films on the plastic parts. It would be better to avoid that letters and small details go on the areas that have protrusions / recesses.

```html
<!DOCTYPE html>
<html lang="en">
<head>
<meta charset="utf-8">
<title>Vallecrestia Van Wrap</title>
<link rel="stylesheet" href="https://fonts.googleapis.com/css2?family=Poppins:wght@500;600&display=swap">
<style>
  :root {
    --van-black: #0c0c0c;
    --band-white: #f4f4f4;
    --alpine-green: #0e4a3a;
    --ink: #111111;
    --page: #ffffff;
  }
  html, body {
    margin: 0;
    padding: 0;
    width: 1200px;
    height: 1200px;
    overflow: hidden;
    background: var(--page);
  }
  .wrap-canvas {
    display: block;
    width: 1200px;
    height: 1200px;
  }
  .wrap-body { fill: var(--van-black); }
  .wrap-band { fill: var(--band-white); }
  .wrap-green { fill: var(--alpine-green); }
  .brand-square { fill: none; stroke: var(--band-white); stroke-width: 4; }
  .brand-name {
    font-family: "Poppins", sans-serif;
    font-weight: 500;
    font-size: 58px;
    letter-spacing: 7px;
    fill: var(--band-white);
  }
  .contact-phone {
    font-family: "Poppins", sans-serif;
    font-weight: 600;
    font-size: 26px;
    letter-spacing: 1px;
    fill: var(--ink);
  }
  .contact-web {
    font-family: "Poppins", sans-serif;
    font-weight: 600;
    font-size: 19px;
    fill: var(--ink);
  }
  .contact-divider { stroke: var(--alpine-green); stroke-width: 3; }
</style>
</head>
<body>
<svg class="wrap-canvas" viewBox="0 0 1200 1200" xmlns="http://www.w3.org/2000/svg">
  <defs>
    <clipPath id="van-side">
      <rect x="60" y="420" width="1080" height="400" rx="40"/>
    </clipPath>
  </defs>

  <g class="van-side-panel" clip-path="url(#van-side)">
    <rect class="wrap-body" x="60" y="420" width="1080" height="400"/>

    <g class="diagonal-graphics" transform="rotate(-12 460 760)">
      <polygon class="wrap-band" points="430,778 472,730 1300,730 1300,778"/>
      <polygon class="wrap-green" points="455,788 1300,788 1300,1200 250,1200"/>

      <text class="brand-name" x="470" y="715">VALLECRESTIA</text>

      <text class="contact-phone" x="535" y="765">0342 555 018</text>
      <line class="contact-divider" x1="738" y1="740" x2="738" y2="770"/>
      <text class="contact-web" x="758" y="764">www.vallecrestia.com</text>
    </g>

    <rect class="brand-square" x="310" y="652" width="84" height="84"/>
  </g>
</svg>
</body>
</html>
```